Marcus Lindqvist Photography needs a business card designs

I am looking for a business card with a logo clean and simple which I can use that logo on my website or on my pictures. It has to be very classy and very professional. Please look at my website at www.marcuslvqphoto.com for my signature. I'm thinking of something like that for my signature/logo. I'm still working on my website but you get an idea. I'm open to any design but not too busy graphics.

I will be printing the business card from qrivel.com.

Surprise me :)

contact me if you have any questions.

-ML

I'm receiving a lot of black background at the moment. I know my website is all black doesn't mean I want my card to be all black. Please send in with some white background as well. Thanks :)

check out some business cards that I found online. I think they are simple and look really awesome. I don't want a card that is too busy.

http://www.marcuslvqphoto.com/p270092084

Reason: Please extend the date for me. I haven't really receive any good design yet.

Printing

• -a logo that related to my first and last initial of my name "ML"
-double sided
• -I don't want my background to be all black.
-no pictures on the card

```html
<!DOCTYPE html>
<html lang="en">
<head>
<meta charset="utf-8">
<title>Marcus Lindqvist Photography – Business Card</title>
<link rel="stylesheet" href="https://fonts.googleapis.com/css2?family=Give+You+Glory&family=Open+Sans:wght@300&display=swap">
<style>
  :root {
    --page-bg: #ffffff;
    --card-front: #ffffff;
    --card-back: #f58222;
    --card-edge: #8a8a8a;
    --brand-orange: #f58222;
    --name-grey: #55565a;
    --tagline-grey: #c4c4c4;
    --web-white: #ffffff;
    --mark-faint: rgba(255, 255, 255, 0.10);
  }
  html, body {
    margin: 0;
    padding: 0;
    width: 1200px;
    height: 900px;
    overflow: hidden;
    background: var(--page-bg);
  }
  .canvas {
    position: relative;
    width: 1200px;
    height: 900px;
  }
  .card {
    position: absolute;
    left: 234px;
    top: 20px;
    width: 710px;
    height: 860px;
    border: 1px solid var(--card-edge);
    box-sizing: border-box;
    overflow: hidden;
  }
  .card-front {
    position: absolute;
    left: 0;
    top: 0;
    width: 100%;
    height: 430px;
    background: var(--card-front);
    border-bottom: 1px solid var(--card-edge);
    box-sizing: border-box;
  }
  .brand {
    position: absolute;
    left: 176px;
    top: 172px;
    display: flex;
    align-items: center;
    gap: 22px;
  }
  .brand-square {
    width: 58px;
    height: 58px;
    background: var(--brand-orange);
  }
  .brand-name {
    font-family: "Give You Glory", cursive;
    font-size: 38px;
    color: var(--name-grey);
    line-height: 1;
    white-space: nowrap;
  }
  .tagline {
    position: absolute;
    left: 62px;
    right: 62px;
    top: 360px;
    display: flex;
    justify-content: space-between;
    font-family: "Open Sans", sans-serif;
    font-weight: 300;
    font-size: 26px;
    color: var(--tagline-grey);
    line-height: 1;
  }
  .card-back {
    position: absolute;
    left: 0;
    top: 430px;
    width: 100%;
    height: 430px;
    background: var(--card-back);
  }
  .back-mark {
    position: absolute;
    left: 263px;
    top: 133px;
    width: 166px;
    height: 166px;
    background: var(--mark-faint);
  }
  .website {
    position: absolute;
    left: 0;
    right: 0;
    top: 196px;
    text-align: center;
    font-family: "Give You Glory", cursive;
    font-size: 30px;
    letter-spacing: 3px;
    color: var(--web-white);
    line-height: 1;
  }
</style>
</head>
<body>
  <div class="canvas">
    <div class="card">
      <section class="card-front">
        <div class="brand">
          <div class="brand-square"></div>
          <div class="brand-name">Marcus Lindqvist</div>
        </div>
        <div class="tagline" aria-label="Photography">
          <span>P</span><span>h</span><span>o</span><span>t</span><span>o</span><span>g</span><span>r</span><span>a</span><span>p</span><span>h</span><span>y</span>
        </div>
      </section>
      <section class="card-back">
        <div class="back-mark"></div>
        <div class="website">www.marcuslvqphoto.com</div>
      </section>
    </div>
  </div>
</body>
</html>
```